Speisekarten-Design für mediterranes Restaurant
Zielgruppe
Wir eröffnen am 23.09.2022 ein Restaurant im Hotel SolBrunn Bad Farnhain in 94999 Fürstenzell unter dem Namen 'VELO'. Die Übersetzung aus dem Portugiesischem bedeutet 'Seele' - Velo soll also die Seele des Hauses werden und unsere Gäste aus nah&fern und ob jung oder alt mit mediterranen, besonderen Köstlichkeiten unseres Küchenchefs Matteo Carvalhal verwöhnen.
Auf der Speisekarte stehen Bruch & Frühstück (z.B. Joghurt mit Früchten und Agavensirup, Pancakes und Waffeln, Egg Benedikt aber auch bayerische Spezialitäten wie Weißwurst mit Breze). Weiterhin werden wir Tapas (vegatarisch, Fleisch, Fisch) anbieten. Als USP steht die original portugiesische Cataplana oder Hähnchen nach Art des Hauses auf der Karte. Hinzu kommen noch Desserts. Ebenso benötigen wir eine Wochenkarte sowie eine Getränkekarte (Softdrinks, Kaffee, Tee, Bier, Wein, Long Drinks, etc.) Ich denke eine Seite sollte für Frühstück/Brunch und eine für Vorspeisen, Tapas, Hauptspeisen vorgesehen werden und ein Blatt für die Wochenkarte. Weiterhin ein Blatt mit normalen Getränken und eine Weinkarte.
Wir suchen ein modernes, zeitloses Design für unsere neue Speisekarte. Diese soll auf einzelnen Blättern in einem Klemmbrett aus Holz eingespannt werden. Wichtig ist uns, dass wir die Gerichte und Getränke jederzeit in einem festen Design ändern und selbst drucken können.
Die hochgeladenen Speisekarten im Word-Format dienen nur der Orientierung für Anzahl, etc. Die Karten müssen selbstständig durch uns ergänzt oder geändert werden können. Anbei auch ein Beispielbild, welches über entwurfmarkt.de in Bildwand gefunden wurde.
Aufgabenstellung
als DIN-Format wählen wir A4.
Gerichte wir die Cataplana sollten eine Erklärung beinhalten, die auch noch gut aussieht und nicht nur in Klammern unter dem Gericht steht.

```html
<!DOCTYPE html>
<html lang="de">
<head>
<meta charset="utf-8">
<title>VELO – Frühstück &amp; Brunch</title>
<link rel="stylesheet" href="https://fonts.googleapis.com/css2?family=Alike&family=Cormorant+Garamond:wght@500&display=swap">
<style>
:root{
  --green:#3e5a50;
  --sage:#cfd2ac;
  --ornament:#d3d9b8;
  --paper:#ffffff;
  --backdrop:#e8e8e5;
}
*{box-sizing:border-box;margin:0;padding:0}
html,body{width:1200px;height:2400px;overflow:hidden;background:var(--backdrop)}
body{position:relative;font-family:"Alike",Georgia,serif;color:var(--green)}
.menu-page{
  position:absolute;left:0;top:351px;width:1022px;height:1445px;
  transform:scale(1.1742);transform-origin:0 0;background:var(--paper);
}
.wheat{position:absolute;top:100px;height:86px;background:linear-gradient(180deg,var(--ornament),#e3e8cf);border-radius:4px}
.wheat--left{left:58px;width:272px}
.wheat--right{left:688px;width:268px}
.brand{position:absolute;left:0;right:0;top:96px;text-align:center;font-family:"Cormorant Garamond",Georgia,serif;font-weight:500;font-size:96px;letter-spacing:6px;line-height:1}
.frame{position:absolute;left:0;top:0}
.hero-band{position:absolute;left:80px;top:227px;width:858px;height:92px;background:var(--sage);text-align:center}
.hero-band h1{font-weight:400;font-size:44px;line-height:1;margin-top:18px;letter-spacing:.5px}
.hero-band p{font-size:19px;margin-top:2px}
.bakery-stripes{position:absolute;left:110px;top:345px;width:90px;height:144px;
  background:repeating-linear-gradient(180deg,var(--green) 0 1.5px,var(--sage) 1.5px 5px)}
.bakery-title{position:absolute;left:320px;width:384px;top:328px;text-align:center;font-size:28px;font-weight:400;letter-spacing:.5px;background:var(--paper)}
.item{display:flex;align-items:baseline;white-space:nowrap}
.item .dots{flex:1;border-bottom:2px dotted var(--green);margin:0 3px;transform:translateY(-4px);opacity:.45}
.bakery-list{position:absolute;top:364px;font-size:22px;line-height:27.5px;list-style:none}
.bakery-list--left{left:212px;width:312px}
.bakery-list--right{left:580px;width:318px}
.dish{position:absolute;width:362px}
.dish--left{left:116px}
.dish--right{left:558px;width:342px}
.dish-name{font-size:26px;line-height:30px}
.dish-name .dots{transform:translateY(-6px)}
.dish-desc{font-size:16.5px;line-height:19px}
.extra{font-size:16.5px;line-height:19px}
.extra .price{font-size:15px}
.section-band{position:absolute;height:38px;background:var(--sage);display:flex;align-items:center;justify-content:center;gap:18px;font-size:30px;letter-spacing:.5px}
.section-band svg{width:20px;height:12px}
</style>
</head>
<body>
<div class="menu-page">
  <div class="wheat wheat--left" role="img" aria-label="Ornament aus Weizenähren"></div>
  <div class="wheat wheat--right" role="img" aria-label="Ornament aus Weizenähren"></div>
  <div class="brand">VELO</div>

  <svg class="frame" width="1022" height="1445" viewBox="0 0 1022 1445" fill="none" stroke="var(--green)">
    <path stroke-width="4" stroke-linejoin="miter" d="M120 205 H902 V220 A61 61 0 0 0 963 281 V1334 A61 61 0 0 0 902 1395 V1410 H120 V1395 A63 63 0 0 0 57 1332 V283 A63 63 0 0 0 120 220 Z"/>
    <rect x="80" y="227" width="858" height="1155" stroke-width="2"/>
    <path stroke-width="3.5" d="M318 345 H110 V490 H923 V372 A27 27 0 0 0 896 345 H706"/>
  </svg>

  <header class="hero-band">
    <h1>Frühstück &amp; Brunch</h1>
    <p>Von 8:00 bis 13:00 Uhr</p>
  </header>

  <div class="bakery-stripes"></div>
  <h2 class="bakery-title">FRISCHE BACKWAREN</h2>
  <ul class="bakery-list bakery-list--left">
    <li class="item"><span>Gemischtes Brot</span><span class="dots"></span><span>2,5</span></li>
    <li class="item"><span>Breze</span><span class="dots"></span><span>1,5</span></li>
    <li class="item"><span>Croissant</span><span class="dots"></span><span>2</span></li>
    <li class="item"><span>Franzbrötchen</span><span class="dots"></span><span>2</span></li>
  </ul>
  <ul class="bakery-list bakery-list--right">
    <li class="item"><span>Pain au Chocolat</span><span class="dots"></span><span>2</span></li>
    <li class="item"><span>Quiche</span><span class="dots"></span><span>4</span></li>
    <li class="item"><span>Kuchen</span><span class="dots"></span><span>3,5</span></li>
  </ul>

  <div class="dish dish--left" style="top:498px">
    <div class="dish-name item"><span>Süßer Beginn</span><span class="dots"></span><span>5,5</span></div>
    <p class="dish-desc">Obstsalat, Croissant (Marmelade,<br>Nussella &amp; Honig), Minijogurt/Bircher Müsli</p>
  </div>
  <div class="dish dish--left" style="top:582px;width:360px">
    <div class="dish-name item"><span>Pancakes &amp; Waffeln</span><span class="dots"></span><span>8,5</span></div>
    <p class="dish-desc">mit Puderzucker &amp; Ahornsirup (vegan)</p>
    <div class="extra item"><span>Schoko</span><span class="dots"></span><span class="price">+1</span></div>
    <div class="extra item"><span>Blaubeer</span><span class="dots"></span><span class="price">+1</span></div>
    <div class="extra item"><span>All in one</span><span class="dots"></span><span class="price">+2</span></div>
  </div>
  <div class="dish dish--right" style="top:498px">
    <div class="dish-name item"><span>Bircher Müsli</span><span class="dots"></span><span>6,5</span></div>
    <p class="dish-desc">auf Hafermilch-Basis, dazu frische<br>Früchte, Zimt &amp; schwarzer Sesam</p>
  </div>
  <div class="dish dish--right" style="top:580px;width:346px">
    <div class="dish-name">Joghurt mit frischen</div>
    <div class="dish-name item"><span>Früchten &amp; Agavensirup 5,5</span></div>
    <div class="extra item" style="margin-top:3px"><span>mit Granola</span><span class="dots"></span><span class="price">1</span></div>
    <div class="extra item"><span>mit Sojajoghurt statt Kuh</span><span class="dots"></span><span class="price">1</span></div>
  </div>

  <div class="section-band" style="left:116px;width:786px;top:706px">
    <svg viewBox="0 0 20 12"><circle cx="12" cy="6" r="4" fill="none" stroke="var(--green)" stroke-width="2"/><path d="M0 6h8" stroke="var(--green)" stroke-width="2"/></svg>
    <span>BIO-EIER VOM GLÜCKLICHEN HUHN</span>
    <svg viewBox="0 0 20 12"><circle cx="8" cy="6" r="4" fill="none" stroke="var(--green)" stroke-width="2"/><path d="M12 6h8" stroke="var(--green)" stroke-width="2"/></svg>
  </div>
  <div class="dish dish--left" style="top:752px">
    <div class="dish-name item"><span>Eier im Glas</span><span class="dots"></span><span>5,5</span></div>
    <p class="dish-desc">zwei pochierte Eier im Glas auf Salatbett<br>mit Kräutern &amp; Granatapfel, dazu Brot</p>
  </div>
  <div class="dish dish--left" style="top:820px;width:360px">
    <div class="dish-name item"><span>Egg Benedict</span><span class="dots"></span><span>9,5</span></div>
    <p class="dish-desc" style="margin-top:2px">English Muffin Toastie mit Avocado<br>Creme, Serrano Schinken und<br>hausgemachter Sauce Hollandaise</p>
    <div class="extra item"><span>mit halber Avocado</span><span class="dots"></span><span class="price">1,5</span></div>
    <div class="extra item"><span>mit karamellisierten Tomaten</span><span class="dots"></span><span class="price">1</span></div>
    <div class="extra item"><span>mit Speck</span><span class="dots"></span><span class="price">1,5</span></div>
  </div>
  <div class="dish dish--right" style="top:752px">
    <div class="dish-name item"><span>Rührei / Spiegeleier</span><span class="dots"></span><span>5</span></div>
    <div class="extra item"><span>mit gebratenem Speck</span><span class="dots"></span><span class="price">1,5</span></div>
    <div class="extra item"><span>mit karamellisierten Tomaten</span><span class="dots"></span><span class="price">1</span></div>
    <div class="extra item"><span>mit Räucherlachs</span><span class="dots"></span><span class="price">2,5</span></div>
  </div>
  <div class="dish dish--right" style="top:840px">
    <div class="dish-name item"><span>Egg Royale</span><span class="dots"></span><span>9,5</span></div>
    <p class="dish-desc" style="margin-top:2px">English Muffin Toastie mit Avocado<br>Creme, Räucherlachs und hausgemachter<br>Sauce Hollandaise</p>
    <div class="extra item"><span>mit halber Avocado</span><span class="dots"></span><span class="price">1,5</span></div>
    <div class="extra item"><span>mit karamellisierten Tomaten</span><span class="dots"></span><span class="price">1</span></div>
  </div>

  <div class="section-band" style="left:118px;width:786px;top:986px">
    <svg viewBox="0 0 20 12"><circle cx="12" cy="6" r="4" fill="none" stroke="var(--green)" stroke-width="2"/><path d="M0 6h8" stroke="var(--green)" stroke-width="2"/></svg>
    <span>EINFACH WEIL ES GUT IST</span>
    <svg viewBox="0 0 20 12"><circle cx="8" cy="6" r="4" fill="none" stroke="var(--green)" stroke-width="2"/><path d="M12 6h8" stroke="var(--green)" stroke-width="2"/></svg>
  </div>
  <div class="dish" style="left:118px;width:358px;top:1034px">
    <div class="dish-name item"><span>Käsebrett</span><span class="dots"></span><span>7,5</span></div>
    <p class="dish-desc">Edamer, Brie &amp; Obazda</p>
  </div>
  <div class="dish" style="left:118px;width:358px;top:1082px">
    <div class="dish-name">Lachsteller mit frischem</div>
    <div class="dish-name item"><span>Kren und Zitrone</span><span class="dots"></span><span>8,5</span></div>
  </div>
  <div class="dish" style="left:119px;width:357px;top:1140px">
    <div class="dish-name item"><span>Frühschoppen</span><span class="dots"></span><span>5,5</span></div>
    <p class="dish-desc" style="margin-top:2px">2 Stück Weißwürscht mit Brezn, süßem<br>Senf &amp; Butter</p>
  </div>
  <div class="dish" style="left:119px;width:357px;top:1216px">
    <div class="dish-name item"><span>Shakshuka</span><span class="dots"></span><span>8,5</span></div>
    <p class="dish-desc">israelisches Frühstück aus<br>selbstgemachtem orientalischen<br>Tomatensugo, zwei gestockten Eiern,<br>Zwiebeln, Paprika &amp; dazu Brot</p>
  </div>
  <div class="dish dish--right" style="top:1034px">
    <div class="dish-name item"><span>Wurstbrett</span><span class="dots"></span><span>7,5</span></div>
    <p class="dish-desc">Serrano-, Puten- &amp; Rinderschinken</p>
  </div>
  <div class="dish dish--right" style="top:1084px;width:346px">
    <div class="dish-name item"><span>Avocado Stulle</span><span class="dots"></span><span>6,5</span></div>
    <p class="dish-desc">Sauerteigbrot mit halber Avocado,<br>Avocado Creme, gemischtem Salat</p>
    <div class="extra item" style="padding-right:6px"><span>mit Serrano-Schinken</span><span class="dots"></span><span class="price">2</span></div>
    <div class="extra item" style="padding-right:6px"><span>mit Räucherlachs</span><span class="dots"></span><span class="price">2,5</span></div>
    <div class="extra item" style="padding-right:6px"><span>mit Spiegelei / Rührei</span><span class="dots"></span><span class="price">2</span></div>
  </div>
  <div class="dish dish--right" style="top:1215px">
    <div class="dish-name item"><span>Frühstück für Zwei</span><span class="dots"></span><span>45</span></div>
    <p class="dish-desc" style="margin-top:2px">Brotkörberl + 2 Croissant + Butter<br>Wurstbrett + Käsebrett Rühei<br>Pancake "all in one" Obstsalat,<br>Marmelade, Honig &amp; Nussella<br>2 x 0,1L frisch gepresster<br>Orangensaft + 2 x Heißgetränk</p>
  </div>
</div>
</body>
</html>
```